Kalvoria - a property developer - Website design

Hi all!
Exciting new project for you! :)
We are looking for some creative/modern designs to best represent us as a company.
Please have a look at the following link: huhu.kalvoria.example to get an idea about who we are and what we do.
The 'Main Page' of the HP should be neatly arranged, easy to navigate, contain several pictures (changing every 10 seconds or so) that should reflect that we are property developers.
The navigation points ('About us', 'Projects' 'Investment', 'Contact Us', 'Legal Notice') should be included in the Design (again under every navigation point, pictures may be added - that reflect our profession and/or the subsection)
What we will need at the end of the day is a fully functional site - i.e: a site that is designed and programmed with backend/wordpress, to allow us to make changes anytime we feel like it.
Further questions?! Don't hesitate to contact me! Thanks :)
Target Market(s)
Real Estate Development/Building sector
Industry/Entity Type
Real Estate Development
Number of Pages Required
5+ page
Look and feel

```html
<!DOCTYPE html>
<html lang="en">
<head>
<meta charset="utf-8">
<title>Kalvoria – Property Developer</title>
<link href="https://fonts.googleapis.com/css2?family=Open+Sans:wght@300;400;600;700&display=swap" rel="stylesheet">
<style>
:root{
  --blue:#2f7fd3;
  --blue-dark:#2367b0;
  --footer-blue:#3a86d2;
  --footer-bar:#2c6fb5;
  --ink:#333;
  --muted:#777;
  --line:#dcdcdc;
  --panel:#f3f3f3;
  --white:#fff;
}
*{box-sizing:border-box;margin:0;padding:0}
html,body{width:1200px;height:3586px;overflow:hidden}
body{font-family:"Open Sans",Arial,sans-serif;color:var(--ink);background:var(--white);font-size:13px;line-height:1.55}
.wrap{width:1068px;margin:0 auto;position:relative}
.sq{display:inline-block;width:14px;height:14px;background:#c9c9c9;border-radius:2px}

.topbar{height:34px;background:#f6f6f6;border-bottom:1px solid #e8e8e8;font-size:11px;color:var(--muted)}
.topbar .wrap{display:flex;align-items:center;height:34px;gap:28px}
.topbar .social{margin-left:auto;display:flex;gap:14px}

.nav{height:66px;border-bottom:1px solid #e6e6e6}
.nav .wrap{display:flex;align-items:center;height:66px}
.logo{display:flex;align-items:center;gap:8px;font-weight:700;font-size:22px;color:var(--blue);letter-spacing:1px}
.logo .mark{width:20px;height:20px;background:var(--blue)}
.menu{display:flex;margin-left:58px;height:66px}
.menu a{font-size:11px;color:#555;text-decoration:none;padding:0 18px;display:flex;align-items:center;border-top:3px solid transparent}
.menu a.active{border-top-color:var(--blue);color:var(--blue)}
.account{margin-left:auto;display:flex;gap:10px;padding-left:20px;border-left:1px solid #e6e6e6;height:66px;align-items:center}
.account span{font-size:10px;font-weight:600;border:1px solid #ccc;padding:6px 18px;color:#555}

.hero{height:470px;position:relative;background:linear-gradient(100deg,#6a6a6a 0%,#8f8f8c 35%,#b9b5ac 60%,#7d7a74 100%)}
.hero-text{position:absolute;left:67px;top:80px;width:470px}
.hero-text h1{display:inline-block;background:rgba(255,255,255,.85);font-size:44px;font-weight:600;padding:0 14px;color:#444;line-height:64px}
.hero-text p{background:rgba(255,255,255,.85);padding:10px 14px;font-size:14px;color:#555;margin-top:4px}
.hero-actions{display:flex;align-items:center;gap:22px;margin-top:18px}
.btn-ghost{background:rgba(255,255,255,.85);font-size:11px;font-weight:600;padding:10px 36px;color:#555}
.or{font-size:11px;color:#eee}
.btn-blue{background:var(--blue);color:#fff;font-size:11px;font-weight:600;padding:10px 42px}
.price-tag{position:absolute;left:908px;top:263px;background:rgba(120,120,120,.7);color:#fff;font-size:40px;font-weight:300;padding:0 12px;line-height:60px}
.tabs{position:absolute;left:67px;right:65px;bottom:0;height:70px;background:var(--blue);display:flex;align-items:center}
.tabs span{color:#fff;font-size:11px;font-weight:600;padding:0 30px;height:70px;display:flex;align-items:center}
.tabs .active{background:var(--blue-dark);padding:0 30px;width:163px}
.tabs .all{margin-left:auto;margin-right:20px;background:#fff;color:var(--blue);height:auto;padding:8px 26px;font-size:10px}

.search{width:1068px;margin:0 auto;height:202px;border:1px solid var(--line);border-top:0;padding:22px 20px;display:grid;grid-template-columns:repeat(4,1fr);row-gap:18px;column-gap:28px}
.field label{display:block;font-size:11px;font-weight:600;margin-bottom:6px}
.field .input{height:36px;border:1px solid #d3d3d3;font-size:12px;color:#555;padding:0 10px;display:flex;align-items:center;justify-content:space-between}
.field .input::after{content:"";width:0;height:0;border:5px solid transparent;border-top-color:#999;margin-top:5px}
.row1{display:grid;grid-template-columns:322px 322px 325px;gap:28px;grid-column:1/-1}
.row2{display:grid;grid-template-columns:234px 234px 234px 234px;gap:28px;grid-column:1/-1}
.range{position:relative;height:36px}
.range .vals{display:flex;justify-content:flex-end;gap:8px;font-size:10px;position:absolute;right:0;top:-26px}
.range .vals span{border:1px solid #ccc;padding:1px 8px}
.range .track{position:absolute;left:0;right:0;top:12px;height:5px;background:#ddd}
.range .fill{position:absolute;left:60px;right:95px;top:12px;height:5px;background:var(--blue)}
.range .knob{position:absolute;top:6px;width:16px;height:16px;border:1px solid #bbb;background:#fff;border-radius:50%}
.range .scale{position:absolute;top:24px;left:0;right:0;display:flex;justify-content:space-between;font-size:9px;color:#aaa}
.btn-find{align-self:end;height:36px;background:var(--blue);color:#fff;font-size:11px;font-weight:600;display:flex;align-items:center;justify-content:center}

.intro{height:251px;text-align:center;padding-top:68px}
.intro h2{font-size:34px;font-weight:300;color:#444}
.intro h2 b{font-weight:600}
.intro p{width:900px;margin:14px auto 0;font-size:14px;color:var(--muted)}

.recent{height:550px;background:var(--panel);border-top:1px solid #e2e2e2;border-bottom:1px solid #e2e2e2;padding-top:62px}
.section-title{font-size:15px;font-weight:400;color:var(--blue);padding-bottom:6px;border-bottom:1px solid #d6d6d6;position:relative}
.section-title::after{content:"";position:absolute;left:0;bottom:-1px;width:170px;height:2px;background:var(--blue)}
.cards{display:flex;gap:34px;margin-top:30px;padding-left:5px}
.card{width:240px;height:330px;background:#fff;border:1px solid #ddd;padding:10px}
.card .photo{height:148px;position:relative}
.card .tag{position:absolute;left:4px;top:4px;background:var(--blue);color:#fff;font-size:9px;font-weight:700;padding:2px 6px}
.card h3{font-size:13px;font-weight:600;margin-top:12px}
.card .loc{font-size:12px;color:var(--muted);padding-bottom:10px;border-bottom:1px solid #e6e6e6;margin-top:4px}
.card .deal{display:flex;justify-content:space-between;align-items:center;margin-top:10px}
.card .status{background:#ddd;color:#fff;font-size:10px;font-weight:700;padding:3px 8px}
.card .price{font-size:22px;color:var(--blue);font-weight:600}
.card .meta{display:flex;border:1px solid #e6e6e6;margin-top:10px;font-size:9px;color:#999}
.card .meta span{flex:1;padding:5px 6px;display:flex;align-items:center;gap:4px;border-right:1px solid #e6e6e6}
.card .meta span:last-child{border:0}
.card .meta i{width:7px;height:7px;background:#bbb;display:inline-block}

.how{height:521px;text-align:center;padding-top:60px}
.how h2{font-size:34px;font-weight:300;color:#444}
.how h2 b{font-weight:600}
.steps{display:flex;justify-content:center;gap:50px;margin-top:28px;position:relative}
.step{width:320px}
.bubble{width:146px;height:160px;margin:0 auto}
.step h4{font-size:12px;font-weight:600;margin-top:14px}
.step p{font-size:12px;color:var(--muted);margin-top:6px}
.curve{position:absolute;top:55px}

.agents{height:492px;position:relative;background:linear-gradient(90deg,#c7d3bf 0%,#9fae96 30%,#a5a69c 55%,#8fa684 80%,#bfcfa9 100%)}
.agents .row{position:absolute;left:0;right:0;top:69px;display:flex;justify-content:center;gap:85px}
.agent{width:190px;text-align:center;color:#fff}
.portrait{width:190px;height:200px}
.agent h4{font-size:12px;font-weight:600;margin-top:16px}
.agent p{font-size:12px;margin-top:4px;line-height:1.45}
.agent .social{display:flex;justify-content:center;gap:10px;margin-top:10px}
.agent .social .sq{background:#f2f2f2;width:22px;height:22px}

.news{height:424px;padding-top:62px}
.news .wrap{display:flex;gap:28px}
.news .col{flex:1}
.post{display:flex;gap:20px;padding:26px 0 20px;border-bottom:1px solid #e6e6e6}
.post:last-child{border:0}
.thumb{width:105px;height:72px;flex:none}
.post .body{flex:1}
.post h5{font-size:12px;font-weight:700;text-transform:uppercase}
.post p{font-size:12px;color:var(--muted);margin-top:4px}
.post .foot{display:flex;justify-content:space-between;align-items:center;margin-top:8px;font-size:11px;color:#666}
.more{border:1px solid #ccc;font-size:9px;font-weight:700;padding:4px 18px;color:#777}
.quote{display:flex;gap:20px;padding:26px 0 20px;border-bottom:1px solid #e6e6e6}
.quote:last-child{border:0}
.avatar{width:103px;height:103px;flex:none}
.quote h5{font-size:12px;font-weight:600}
.quote p{font-size:12px;color:var(--muted);margin-top:8px}

.cta{height:221px;padding-top:25px}
.cta .box{height:132px;background:#eee;border:1px solid #e2e2e2;display:flex;align-items:center;padding:0 30px}
.cta h3{font-size:26px;font-weight:300;color:#444}
.cta h3 b{font-weight:700}
.cta p{font-size:13px;color:var(--muted);margin-top:4px}
.cta .btn-blue{margin-left:auto;padding:10px 44px}

.footer{height:306px;background:var(--footer-blue);color:#fff;padding-top:54px}
.footer .wrap{display:flex}
.fcol{width:272px;font-size:12px;line-height:1.5}
.fcol h6{font-size:12px;font-weight:700;margin-bottom:14px}
.fcol .line{display:flex;gap:10px;align-items:center;margin-bottom:16px}
.fcol .time{font-size:10px;font-weight:700;margin:2px 0 10px}
.about{padding-top:62px}
.about .logo{color:#fff;margin-top:14px}
.about .logo .mark{background:#fff}
.newsletter{display:flex;margin-top:14px}
.newsletter .email{width:150px;height:34px;background:#fff;color:#888;padding:0 10px;display:flex;align-items:center;font-size:12px}
.newsletter .send{height:34px;background:var(--footer-bar);padding:0 20px;display:flex;align-items:center;font-size:11px;font-weight:700}
.bottombar{height:49px;background:var(--footer-bar);color:#fff;font-size:10px;font-weight:600}
.bottombar .wrap{display:flex;align-items:center;height:49px}
.bottombar .social{margin-left:auto;display:flex;gap:16px}
.bottombar .sq{background:rgba(255,255,255,.55)}
</style>
</head>
<body>

<header class="topbar">
  <div class="wrap">
    <span>☎ 1-800-555-0142</span>
    <span>✉ info@kalvoria.example</span>
    <div class="social"><i class="sq"></i><i class="sq"></i><i class="sq"></i><i class="sq"></i></div>
  </div>
</header>

<nav class="nav">
  <div class="wrap">
    <div class="logo"><i class="mark"></i>KALVORIA</div>
    <div class="menu">
      <a class="active">HOME</a><a>ABOUT US</a><a>PROJECTS</a><a>INVESTMENT</a><a>CONTACT US</a><a>LEGAL NOTICE</a>
    </div>
    <div class="account"><span>LOGIN</span><span>REGISTER</span></div>
  </div>
</nav>

<section class="hero" role="img" aria-label="Photograph of a modern living room in a newly developed residence">
  <div class="hero-text">
    <h1>580 Harbor St</h1>
    <p>Lorem ipsum dolor sit amet, consectetur adipiscing elit. Nullam eu nisl et lectus tempor pretium pellentesque rhoncus nisl. Sed cursus ante eget orci lorem ipsum sodales.</p>
    <div class="hero-actions">
      <span class="btn-ghost">VIEW PROJECT</span><span class="or">OR</span><span class="btn-blue">CONTACT US</span>
    </div>
  </div>
  <div class="price-tag">$525,000</div>
  <div class="tabs">
    <span class="active">ALL PROJECTS</span><span>FOR SALE</span><span>FOR RENT</span>
    <span class="all">VIEW ALL PROJECTS</span>
  </div>
</section>

<section class="search">
  <div class="row1">
    <div class="field"><label>Project Type</label><div class="input">Any</div></div>
    <div class="field"><label>Location</label><div class="input">Any</div></div>
    <div class="field"><label>Price Range</label>
      <div class="range">
        <div class="vals"><span>$143,000</span>–<span>$545,000</span></div>
        <div class="track"></div><div class="fill"></div>
        <i class="knob" style="left:52px"></i><i class="knob" style="right:88px"></i>
        <div class="scale"><span>0</span><span>$100,000</span></div>
      </div>
    </div>
  </div>
  <div class="row2">
    <div class="field"><label>Beds</label><div class="input">Any</div></div>
    <div class="field"><label>Baths</label><div class="input">Any</div></div>
    <div class="field"><label>Area (Sq Ft)</label><div class="input">Any</div></div>
    <div class="btn-find">FIND PROJECTS</div>
  </div>
</section>

<section class="intro">
  <h2>Modern, solid &amp; <b>lasting</b> developments.</h2>
  <p>Lorem ipsum dolor sit amet, consectetur adipiscing elit. Proin sit amet sagittis erat. Maecenas suscipit ut quam id condimentum. Pellentesque cursus lacinia sapien et laoreet. Ut mattis ultricies sem id elementum. Vestibulum blandit consectetur nibh.</p>
</section>

<section class="recent">
  <div class="wrap">
    <h3 class="section-title">RECENT PROJECTS</h3>
    <div class="cards">
      <article class="card">
        <div class="photo" role="img" aria-label="Photo of a newly built family home with a driveway" style="background:linear-gradient(180deg,#b8c6d3,#7a7d73 60%,#8a8d86)"><span class="tag">FAMILY HOME</span></div>
        <h3>587 Alder Avenue</h3><div class="loc">Fairhaven, NL</div>
        <div class="deal"><span class="status">FOR SALE</span><span class="price">$687,000</span></div>
        <div class="meta"><span><i></i>2,412m</span><span><i></i>4 Beds</span><span><i></i>3 Baths</span></div>
      </article>
      <article class="card">
        <div class="photo" role="img" aria-label="Photo of a wooden apartment building among trees" style="background:linear-gradient(180deg,#c3d0da,#8b6f55 55%,#6d7453)"><span class="tag">APARTMENT</span></div>
        <h3>587 Alder Avenue</h3><div class="loc">Fairhaven, NL</div>
        <div class="deal"><span class="status">FOR RENT</span><span class="price">$1,200/mo</span></div>
        <div class="meta"><span><i></i>2,412m</span><span><i></i>4 Beds</span><span><i></i>3 Baths</span></div>
      </article>
      <article class="card">
        <div class="photo" role="img" aria-label="Photo of a brick condo development" style="background:linear-gradient(180deg,#a9bfd2,#7d5b44 55%,#5f6e4a)"><span class="tag">CONDO</span></div>
        <h3>587 Alder Avenue</h3><div class="loc">Fairhaven, NL</div>
        <div class="deal"><span class="status">FOR SALE</span><span class="price">$687,000</span></div>
        <div class="meta"><span><i></i>2,412m</span><span><i></i>4 Beds</span><span><i></i>3 Baths</span></div>
      </article>
      <article class="card">
        <div class="photo" role="img" aria-label="Photo of a villa with a green lawn" style="background:linear-gradient(180deg,#9fc0df,#8a7a63 50%,#5b8a3c)"><span class="tag">VILLA</span></div>
        <h3>587 Alder Avenue</h3><div class="loc">Fairhaven, NL</div>
        <div class="deal"><span class="status">FOR SALE</span><span class="price">$687,000</span></div>
        <div class="meta"><span><i></i>2,412m</span><span><i></i>4 Beds</span><span><i></i>3 Baths</span></div>
      </article>
    </div>
  </div>
</section>

<section class="how">
  <h2>We make your life <b>easy</b>. Here’s how.</h2>
  <div class="steps">
    <div class="step">
      <svg class="bubble" viewBox="0 0 146 160"><path d="M73 3a70 70 0 1 0 0 140a70 70 0 1 0 0-140z" fill="#fff" stroke="#999" stroke-width="3"/><path d="M63 142l10 15l10-15" fill="#fff" stroke="#999" stroke-width="3"/><rect x="56" y="48" width="32" height="44" fill="#555"/><rect x="60" y="52" width="32" height="44" fill="#777"/></svg>
      <h4>SELECTED PROJECTS</h4>
      <p>Lorem ipsum dolor sit amet, consectetur adipiscing. In metus diam, fermentum in orci sit amet, lobortis congue diam. Interdum et malesuada fames ac ante ipsum primis in faucibus.</p>
    </div>
    <div class="step">
      <svg class="bubble" viewBox="0 0 146 160"><path d="M73 3a70 70 0 1 0 0 140a70 70 0 1 0 0-140z" fill="#fff" stroke="#999" stroke-width="3"/><path d="M63 142l10 15l10-15" fill="#fff" stroke="#999" stroke-width="3"/><circle cx="73" cy="60" r="14" fill="#555"/><path d="M47 98c0-18 12-24 26-24s26 6 26 24z" fill="#555"/></svg>
      <h4>EXPERIENCED TEAM</h4>
      <p>Lorem ipsum dolor sit amet, consectetur adipiscing. In metus diam, fermentum in orci sit amet, lobortis congue diam. Interdum et malesuada fames ac ante ipsum primis in faucibus.</p>
    </div>
    <div class="step">
      <svg class="bubble" viewBox="0 0 146 160"><path d="M73 3a70 70 0 1 0 0 140a70 70 0 1 0 0-140z" fill="#fff" stroke="#999" stroke-width="3"/><path d="M63 142l10 15l10-15" fill="#fff" stroke="#999" stroke-width="3"/><circle cx="73" cy="73" r="24" fill="none" stroke="#555" stroke-width="5"/><path d="M84 62l-7 16l-15 6l7-16z" fill="#555"/></svg>
      <h4>INVESTMENT GUIDANCE</h4>
      <p>Lorem ipsum dolor sit amet, consectetur adipiscing. In metus diam, fermentum in orci sit amet, lobortis congue diam. Interdum et malesuada fames ac ante ipsum primis in faucibus.</p>
    </div>
    <svg class="curve" style="left:360px" width="110" height="40" viewBox="0 0 110 40"><path d="M4 30Q55 -6 100 24" fill="none" stroke="#aaa" stroke-width="2"/><path d="M92 16l9 9l-12 2" fill="none" stroke="#aaa" stroke-width="2"/></svg>
    <svg class="curve" style="left:730px" width="110" height="40" viewBox="0 0 110 40"><path d="M4 30Q55 -6 100 24" fill="none" stroke="#aaa" stroke-width="2"/><path d="M92 16l9 9l-12 2" fill="none" stroke="#aaa" stroke-width="2"/></svg>
  </div>
</section>

<section class="agents" role="img" aria-label="Blurred office background behind the team portraits">
  <div class="row">
    <div class="agent">
      <svg class="portrait" viewBox="0 0 190 200" role="img" aria-label="Portrait photo of team member John Doe"><circle cx="95" cy="95" r="91" fill="#fff"/><circle cx="95" cy="95" r="83" fill="#7fa0bf"/><path d="M85 185l10 13l10-13" fill="#fff"/></svg>
      <h4>JOHN DOE</h4><p>Lorem ipsum dolor sit amet, consectetur adipiscing elit. Sed purus eget nunc.</p>
      <div class="social"><i class="sq"></i><i class="sq"></i><i class="sq"></i><i class="sq"></i></div>
    </div>
    <div class="agent">
      <svg class="portrait" viewBox="0 0 190 200" role="img" aria-label="Portrait photo of team member Steve Marlow"><circle cx="95" cy="95" r="91" fill="#fff"/><circle cx="95" cy="95" r="83" fill="#8c7a6a"/><path d="M85 185l10 13l10-13" fill="#fff"/></svg>
      <h4>STEVE MARLOW</h4><p>Lorem ipsum dolor sit amet, consectetur adipiscing elit. Sed purus eget nunc.</p>
      <div class="social"><i class="sq"></i><i class="sq"></i><i class="sq"></i><i class="sq"></i></div>
    </div>
    <div class="agent">
      <svg class="portrait" viewBox="0 0 190 200" role="img" aria-label="Portrait photo of team member Walter Brandt"><circle cx="95" cy="95" r="91" fill="#fff"/><circle cx="95" cy="95" r="83" fill="#a0aeb8"/><path d="M85 185l10 13l10-13" fill="#fff"/></svg>
      <h4>WALTER BRANDT</h4><p>Lorem ipsum dolor sit amet, consectetur adipiscing elit. Sed purus eget nunc.</p>
      <div class="social"><i class="sq"></i><i class="sq"></i><i class="sq"></i><i class="sq"></i></div>
    </div>
    <div class="agent">
      <svg class="portrait" viewBox="0 0 190 200" role="img" aria-label="Portrait photo of team member Sarah Lindqvist"><circle cx="95" cy="95" r="91" fill="#fff"/><circle cx="95" cy="95" r="83" fill="#6b6660"/><path d="M85 185l10 13l10-13" fill="#fff"/></svg>
      <h4>SARAH LINDQVIST</h4><p>Lorem ipsum dolor sit amet, consectetur adipiscing elit. Sed purus eget nunc.</p>
      <div class="social"><i class="sq"></i><i class="sq"></i><i class="sq"></i><i class="sq"></i></div>
    </div>
  </div>
</section>

<section class="news">
  <div class="wrap">
    <div class="col">
      <h3 class="section-title">RECENT BLOG POSTS</h3>
      <div class="post">
        <div class="thumb" role="img" aria-label="Photo of a bright living room interior" style="background:linear-gradient(135deg,#d9d4cc,#8e8375)"></div>
        <div class="body"><h5>Awesome dream house in a great location</h5><p>Lorem ipsum dolor sit amet, consectetur adipiscing elit. Quisque eget ante vel nunc posuere rhoncus. Donec quis elit in.</p>
        <div class="foot"><span class="more">READ MORE</span><span>Feb 5, 2014</span></div></div>
      </div>
      <div class="post">
        <div class="thumb" role="img" aria-label="Photo of a living room with warm lighting" style="background:linear-gradient(135deg,#c9b59c,#5f4d3e)"></div>
        <div class="body"><h5>Awesome dream house in a great location</h5><p>Lorem ipsum dolor sit amet, consectetur adipiscing elit. Quisque eget ante vel nunc posuere rhoncus. Donec quis elit in.</p>
        <div class="foot"><span class="more">READ MORE</span><span>Feb 5, 2014</span></div></div>
      </div>
    </div>
    <div class="col">
      <h3 class="section-title">TESTIMONIALS</h3>
      <div class="quote">
        <div class="avatar" role="img" aria-label="Photo of a client at a desk" style="background:linear-gradient(135deg,#9aa6b0,#4c5157)"></div>
        <div><h5>JOHN DOE</h5><p>Lorem ipsum dolor sit amet, consectetur adipiscing elit. Morbi vehicula dapibus mauris, quis ullamcorper enim aliquet sed. Maecenas eget tellus ut. Vivamus condimentum egestas nulla quis velit sed justo turpis, commodo sit amet.</p></div>
      </div>
      <div class="quote">
        <div class="avatar" role="img" aria-label="Photo of a client in an office" style="background:linear-gradient(135deg,#a9c1d6,#4f6f93)"></div>
        <div><h5>JOHN DOE</h5><p>Lorem ipsum dolor sit amet, consectetur adipiscing elit. Morbi vehicula dapibus mauris, quis ullamcorper enim aliquet sed. Maecenas eget tellus ut. Vivamus condimentum egestas nulla quis velit sed justo turpis, commodo sit amet.</p></div>
      </div>
    </div>
  </div>
</section>

<section class="cta">
  <div class="wrap box">
    <div><h3>Get started today for a <b>free</b> home evaluation!</h3>
    <p>Lorem ipsum dolor sit amet, consectetur adipiscing elit. Quisque eget ante vel nunc lorem ipsum rhoncus.</p></div>
    <span class="btn-blue">CONTACT US</span>
  </div>
</section>

<footer class="footer">
  <div class="wrap">
    <div class="fcol about">
      <p>Lorem ipsum dolor sit amet, consectetur adipiscing elit. Sed ut purus eget nunc ut dignissim vitae hendrerit diam.</p>
      <div class="logo"><i class="mark"></i>KALVORIA</div>
    </div>
    <div class="fcol">
      <h6>CONTACT</h6>
      <div class="line"><svg width="12" height="16" viewBox="0 0 12 16"><path d="M6 0a6 6 0 0 0-6 6c0 4 6 10 6 10s6-6 6-10a6 6 0 0 0-6-6z" fill="#fff"/><circle cx="6" cy="6" r="2" fill="#3a86d2"/></svg>48 Linden Row, Alder Bay</div>
      <div class="line"><svg width="14" height="14" viewBox="0 0 14 14"><path d="M3 1l3 3l-2 2c1 2 2 3 4 4l2-2l3 3l-2 2C6 13 1 8 1 3z" fill="#fff"/></svg>+1 555 010 8901</div>
      <div class="line"><svg width="14" height="10" viewBox="0 0 14 10"><rect width="14" height="10" fill="#fff"/><path d="M0 0l7 6l7-6" fill="none" stroke="#3a86d2"/></svg>hello@kalvoria.example</div>
    </div>
    <div class="fcol">
      <h6>TWITTER</h6>
      <p>@kalvoria Lorem ipsum dolor sit amet, adipiscing elit. Sed purus eget tellus.</p>
      <div class="time">5 MINUTES AGO</div>
      <p>@kalvoria Lorem ipsum dolor sit amet, adipiscing elit. Sed purus eget tellus.</p>
      <div class="time">5 MINUTES AGO</div>
    </div>
    <div class="fcol">
      <h6>NEWSLETTER</h6>
      <p>Lorem ipsum dolor sit amet, consectetur adipiscing elit. Sed ut purus eget nunc ut dignissim cursus at a nisl.</p>
      <div class="newsletter"><span class="email">Your email</span><span class="send">SEND</span></div>
    </div>
  </div>
</footer>

<div class="bottombar">
  <div class="wrap">
    <span>KALVORIA ©COPYRIGHT 2016</span>
    <div class="social"><i class="sq"></i><i class="sq"></i><i class="sq"></i><i class="sq"></i></div>
  </div>
</div>

</body>
</html>
```